Web Design For Metal Recycling Company

We are a scrap and recycling company dealing mainly in scrap metal base in Singapore. We deal in both domestic market and international market. Currently we are still unsure if we want to have a "lively" or "professional" company image so we will leave it to the designer to deem what is good.

We wish for a website to be able to "Retain" the interest of new visitor and at the same time able to give enough information for new and existing customer. We would also wish for design that will get the visitor to "Engage" us.

The attached is the logo for the company and we would want to incorporate that into the website. Either of the logo is fine.

```html
<!DOCTYPE html>
<html lang="en">
<head>
<meta charset="utf-8">
<title>Steelway Recycling</title>
<link href="https://fonts.googleapis.com/css2?family=Oswald:wght@300;400;500&family=Arimo:wght@400;700&display=swap" rel="stylesheet">
<style>
:root{
  --teal-dark:#0c4248;
  --teal:#0f535a;
  --teal-bar:#0d4a50;
  --green:#3db54a;
  --green-dark:#2f9a3c;
  --light:#f4f5f5;
  --white:#ffffff;
  --ink:#222;
  --muted:#555;
  --footer:#151515;
  --gold:#d9a62a;
}
*{margin:0;padding:0;box-sizing:border-box}
html,body{width:1200px;height:2615px;overflow:hidden}
body{font-family:"Arimo",Arial,sans-serif;color:var(--ink);background:var(--white);position:relative}
section,header,footer,nav{position:absolute;left:0;width:1200px}
.center{text-align:center}
h2{font-family:"Oswald",sans-serif;font-weight:300;font-size:50px;letter-spacing:1px}

/* header */
.site-header{top:0;height:108px;background:var(--teal)}
.topbar{position:absolute;top:0;left:0;width:1200px;height:35px;background:var(--teal-dark)}
.phone{position:absolute;right:174px;top:8px;color:#e6eeee;font-size:15px;display:flex;align-items:center;gap:8px}
.brand{position:absolute;left:174px;top:44px;display:flex;align-items:center;gap:12px;color:var(--white);font-family:"Oswald",sans-serif;font-size:22px;font-weight:400}
.brand .mark{width:44px;height:44px;border:3px solid var(--gold);background:#1a5a60}
.main-nav{position:absolute;left:567px;top:35px;display:flex;height:70px}
.main-nav a{font-family:"Oswald",sans-serif;font-size:16px;color:var(--white);text-decoration:none;padding:0 18px;line-height:70px}
.main-nav a.active{background:var(--green)}

/* hero */
.hero{top:108px;height:520px;background:linear-gradient(100deg,#2b5f9a 0%,#6d8fb5 30%,#b9c6cf 45%,#4a7fa8 70%,#8c4a2a 88%,#5d3a22 100%)}
.hero-title{position:absolute;left:203px;top:182px;width:530px;background:rgba(0,0,0,.35);color:var(--white);font-family:"Arimo",sans-serif;font-weight:700;font-size:54px;line-height:62px;padding:2px 8px}
.hero-sub{position:absolute;left:203px;top:392px;background:var(--green);color:var(--white);font-size:26px;padding:8px 10px}
.slider-arrows{position:absolute;left:942px;top:490px;display:flex;gap:4px}
.slider-arrows span{width:32px;height:32px;background:var(--green);color:var(--white);font-size:20px;text-align:center;line-height:30px}

/* welcome */
.welcome{top:628px;height:238px;background:var(--teal-bar);color:var(--white)}
.welcome h2{margin-top:20px}
.welcome p{width:860px;margin:18px auto 0;font-size:15px;line-height:27px;color:#dfe9ea}

/* what we do */
.services-overview{top:866px;height:534px;background:var(--light)}
.services-overview h2{margin-top:48px}
.feature{position:absolute;top:155px;width:240px;text-align:center}
.feature .icon{width:124px;height:124px;margin:0 auto;border-radius:50%;background:var(--teal-bar);border:6px solid #111;display:flex;align-items:center;justify-content:center}
.feature h3{font-family:"Arimo",sans-serif;font-weight:400;font-size:17px;margin-top:30px}
.feature p{font-size:11px;line-height:16px;color:var(--muted);margin-top:12px;text-align:justify}
.read-more{display:block;font-size:11px;color:#333;margin-top:26px;text-decoration:none}

/* services */
.services{top:1400px;height:475px;background:var(--green);color:var(--white)}
.services h2{margin-top:42px}
.services .intro{font-size:16px;margin-top:6px}
.service-card{position:absolute;top:149px;width:266px}
.service-card .photo{height:160px}
.service-card h3{background:var(--white);color:var(--ink);font-size:18px;text-align:center;line-height:35px;font-family:"Arimo",sans-serif}
.service-card p{font-size:12px;line-height:17px;text-align:center;margin-top:14px;color:#f2fff2}
.service-card .read-more{color:var(--white);text-align:center;margin-top:14px}

/* clients */
.clients{top:1875px;height:281px;background:var(--white)}
.clients h2{margin-top:42px}
.client{position:absolute;top:140px;width:150px;text-align:center}
.client .dot{width:70px;height:70px;border-radius:50%;background:var(--green);margin:0 auto}
.client span{display:block;margin-top:10px;font-size:14px;font-weight:700;color:#222}

/* testimonial */
.testimonial{top:2156px;height:274px;background:var(--teal-bar);color:var(--white)}
.testimonial h2{margin-top:40px}
.avatar{position:absolute;left:190px;top:114px;width:96px;height:96px;border-radius:50%;border:4px solid var(--green);background:radial-gradient(circle at 50% 40%,#e8c9a8,#8aa08a)}
.quote{position:absolute;left:335px;top:128px;width:680px;font-style:italic;font-size:13px;line-height:22px;color:#dfe9ea}
.quote .mark{font-family:"Oswald",sans-serif;font-size:44px;position:absolute;color:var(--white)}
.quote .open{left:-32px;top:-20px}
.quote .close{right:90px;top:40px}
.author{position:absolute;right:195px;top:196px;font-style:italic;font-size:14px;color:var(--green)}

/* footer */
.footer-nav{top:2430px;height:46px;background:#0a3338;display:flex;justify-content:center;align-items:center;gap:34px}
.footer-nav a{font-family:"Oswald",sans-serif;font-size:14px;color:var(--white);text-decoration:none}
.footer-nav a.active{color:var(--green)}
.site-footer{top:2476px;height:139px;background:var(--footer);color:#ccc;text-align:center;font-size:13px}
.site-footer .follow{margin-top:22px}
.social{display:flex;justify-content:center;gap:6px;margin-top:10px}
.social span{width:26px;height:26px;background:#3b5f9a;border-radius:3px}
.site-footer .legal{margin-top:16px}
</style>
</head>
<body>

<header class="site-header">
  <div class="topbar">
    <div class="phone">
      <svg width="14" height="14" viewBox="0 0 24 24"><path fill="#e6eeee" d="M6.6 10.8a15 15 0 0 0 6.6 6.6l2.2-2.2a1 1 0 0 1 1-.25 11.4 11.4 0 0 0 3.6.6 1 1 0 0 1 1 1V20a1 1 0 0 1-1 1A17 17 0 0 1 3 4a1 1 0 0 1 1-1h3.5a1 1 0 0 1 1 1c0 1.25.2 2.45.6 3.6a1 1 0 0 1-.25 1z"/></svg>
      01000-555-0123
    </div>
  </div>
  <div class="brand"><span class="mark"></span>Steelway Recycling</div>
  <nav class="main-nav">
    <a class="active" href="#">HOME</a><a href="#">WHAT WE DO</a><a href="#">SERVICES</a><a href="#">LOCATION</a><a href="#">CONTACT US</a>
  </nav>
</header>

<section class="hero" role="img" aria-label="Photo of an older man depositing a bottle into a recycling bank">
  <div class="hero-title">Lorem ipsum dolor sit amet, consectetur</div>
  <div class="hero-sub">Lorem ipsum dolor sit amet, consectetur adipisicing elit</div>
  <div class="slider-arrows"><span>&lt;</span><span>&gt;</span></div>
</section>

<section class="welcome center">
  <h2>WELCOME</h2>
  <p>Lorem ipsum dolor sit amet, consectetur adipisicing elit, sed do eiusmod tempor incididunt ut labore et dolore magna aliqua. Ut enim ad minim veniam, quis nostrud exercitation ullamco laboris nisi ut aliquip ex ea commodo consequat. Duis aute irure dolor in reprehenderit in voluptate velit esse cillum dolore eu fugiat nulla pariatur.</p>
</section>

<section class="services-overview center">
  <h2>WHAT WE DO</h2>
  <div class="feature" style="left:185px">
    <div class="icon"><svg width="54" height="54" viewBox="0 0 24 24"><path fill="none" stroke="var(--green)" stroke-width="2.2" d="M19 12a7 7 0 1 1-2-4.9"/><path fill="var(--green)" d="M20 3v6h-6z"/></svg></div>
    <h3>LOREM IPSUM DOLOR</h3>
    <p>Lorem ipsum dolor sit amet, consectetur adipisicing elit, sed do eiusmod tempor incididunt ut labore et dolore magna aliqua. Ut enim ad minim veniam, quis nostrud exercitation ullamco laboris nisi ut aliquip ex ea commodo consequat. Duis aute irure dolor in reprehenderit in voluptate.</p>
    <a class="read-more" href="#">READ MORE</a>
  </div>
  <div class="feature" style="left:484px">
    <div class="icon"><svg width="54" height="54" viewBox="0 0 24 24"><rect x="6" y="8" width="12" height="14" rx="1" fill="var(--green)"/><rect x="4" y="5" width="16" height="2" fill="var(--green)"/><rect x="10" y="2.5" width="4" height="2" fill="var(--green)"/></svg></div>
    <h3>LOREM IPSUM DOLOR</h3>
    <p>Lorem ipsum dolor sit amet, consectetur adipisicing elit, sed do eiusmod tempor incididunt ut labore et dolore magna aliqua. Ut enim ad minim veniam, quis nostrud exercitation ullamco laboris nisi ut aliquip ex ea commodo consequat. Duis aute irure dolor in reprehenderit in voluptate.</p>
    <a class="read-more" href="#">READ MORE</a>
  </div>
  <div class="feature" style="left:784px">
    <div class="icon"><svg width="60" height="54" viewBox="0 0 28 24"><circle cx="8" cy="8" r="3.5" fill="var(--green)"/><circle cx="20" cy="8" r="3.5" fill="var(--green)"/><circle cx="14" cy="6" r="4" fill="var(--green)"/><path d="M1 20a7 6 0 0 1 12-3H1zM27 20a7 6 0 0 0-12-3h12zM6 21a8 8 0 0 1 16 0z" fill="var(--green)"/></svg></div>
    <h3>LOREM IPSUM DOLOR</h3>
    <p>Lorem ipsum dolor sit amet, consectetur adipisicing elit, sed do eiusmod tempor incididunt ut labore et dolore magna aliqua. Ut enim ad minim veniam, quis nostrud exercitation ullamco laboris nisi ut aliquip ex ea commodo consequat. Duis aute irure dolor in reprehenderit in voluptate.</p>
    <a class="read-more" href="#">READ MORE</a>
  </div>
</section>

<section class="services center">
  <h2>SERVICES</h2>
  <p class="intro">Lorem ipsum dolor sit amet, consectetur adipisicing elit, sed do eiusmod tempor incididunt ut labore et dolore.</p>
  <div class="service-card" style="left:180px">
    <div class="photo" role="img" aria-label="Photo of colourful recycling bins in a row" style="background:linear-gradient(90deg,#2f5fa8,#d8c23a 40%,#c43a2f 65%,#3a9a4a)"></div>
    <h3>LOREM IPSUM DOLOR</h3>
    <p>Sed ut perspiciatis unde omnis iste natus error sit voluptatem accusantium doloremque.</p>
    <a class="read-more" href="#">READ MORE</a>
  </div>
  <div class="service-card" style="left:467px">
    <div class="photo" role="img" aria-label="Photo of workers in hard hats sorting material on a recycling line" style="background:linear-gradient(160deg,#3b5a7a,#d8b22a 45%,#6a7a5a 75%,#3a4a3a)"></div>
    <h3>LOREM IPSUM DOLOR</h3>
    <p>Sed ut perspiciatis unde omnis iste natus error sit voluptatem accusantium doloremque.</p>
    <a class="read-more" href="#">READ MORE</a>
  </div>
  <div class="service-card" style="left:757px">
    <div class="photo" role="img" aria-label="Photo of a smiling business team" style="background:linear-gradient(180deg,#f4f4f4 0%,#e6e2de 40%,#2a2a30 100%)"></div>
    <h3>LOREM IPSUM DOLOR</h3>
    <p>Sed ut perspiciatis unde omnis iste natus error sit voluptatem accusantium doloremque.</p>
    <a class="read-more" href="#">READ MORE</a>
  </div>
</section>

<section class="clients center">
  <h2>OUR CLIENTS</h2>
  <div class="client" style="left:245px"><div class="dot"></div><span>Northfield Metals</span></div>
  <div class="client" style="left:419px"><div class="dot"></div><span>Northfield Metals</span></div>
  <div class="client" style="left:593px"><div class="dot"></div><span>Northfield Metals</span></div>
  <div class="client" style="left:768px"><div class="dot"></div><span>Northfield Metals</span></div>
</section>

<section class="testimonial center">
  <h2>CLIENT TESTIMONIAL</h2>
  <div class="avatar" role="img" aria-label="Portrait photo of the client"></div>
  <div class="quote">
    <span class="mark open">&ldquo;</span>
    Lorem ipsum dolor sit amet, consectetur adipisicing elit, sed do eiusmod tempor incididunt ut labore et dolore magna aliqua. Ut enim ad minim veniam, quis nostrud exercitation ullamco laboris nisi ut aliquip ex ea commodo consequat.
    <span class="mark close">&rdquo;</span>
  </div>
  <div class="author">Daniel</div>
</section>

<nav class="footer-nav">
  <a class="active" href="#">HOME</a><a href="#">WHAT WE DO</a><a href="#">SERVICES</a><a href="#">LOCATION</a><a href="#">CONTACT US</a>
</nav>

<footer class="site-footer">
  <div class="follow">Follow Us</div>
  <div class="social"><span></span><span></span><span></span><span></span></div>
  <div class="legal">Privacy / Copyright</div>
</footer>

</body>
</html>
```